New Wordpress Design Project - Australian native plant nursery

I'm Seeking a wordpress website with landing page with contact details and social links, that page will link to another 4 pages. I'm happy to just add in the information once the template is set up (draft text provided on word doc).
Needing pages of information pages for:
- Nursery, what we carry and that we provide garden design services, pictures of plants and gardens
- Native flowers & what we provide, flower arrangements for weddings, special occasions, pictures
- Giftwear short blurb that we carry local artisan giftwear, pictures
- about us with history of the nursery & pictures
* Also wanting a link for e-gift cards. The link will go to an external page (quillo) so I don’t need to set up the website for purchases.
Social media links
Social links
https://www.facebook.com/TheSilverbrookDell
https://www.instagram.com/thesilverbrookdellnursery

Two local native nursery websites that I like the style of:
https://www.marlowbushlandgrowers.example.au/
https://www.tarbello.example.au/

I'm using two versions of our logo, we have the smaller circle and then the other logo which is stretched out. We have used the second design for our signs at the nursery, I've asked the sign guy for a copy of the design as I don't currently have one. I have vector files of the other design.

We have wordpress set up with elemantor and hosting with hostova, I can send you the logon details once design is confirmed.

Target Market(s)

Anyone who likes gardening, we have a pretty even spread of customers across male/female and all ages

Industry/Entity Type

Garden centre with native plants, flowers and giftwear

Coding

Coded - Design and coding required

Colors
0054AA
0677BA
7BADD7
CADEEF
E8F1F8
0094D4
00A9DD
6FCCEA
C7EBF8
E9F6FB
00AB8E
00BBA5
67D7C9
C6EFE9
E9F9F6

Requirements
Must have
• Organic/modern/minimalist design
Nice to have
• Blue/white/green, flannel flowers as per logo

```html
<!DOCTYPE html>
<html lang="en">
<head>
<meta charset="utf-8">
<title>The Silverbrook Dell — Australian Plants, Flowers and Giftware</title>
<link href="https://fonts.googleapis.com/css2?family=Cormorant+Garamond:wght@400;500;600&family=Lato:wght@400;700&display=swap" rel="stylesheet">
<style>
:root{
  --cream:#f6f1e1;
  --cream-deep:#efe8d2;
  --ink:#2b2b2b;
  --ink-soft:#4a4a4a;
  --teal:#16806f;
  --teal-dark:#0f5f53;
  --blue-panel:#2c5e7e;
  --green-panel:#1d6b55;
  --white:#ffffff;
  --nav-blue:#0677BA;
  --call-green:#00AB8E;
  --footer-bg:#fbf9f3;
  --line:#c9c3b2;
}
*{box-sizing:border-box;margin:0;padding:0}
html,body{width:1200px;height:4700px;overflow:hidden}
body{background:var(--cream);font-family:"Lato",Arial,sans-serif;color:var(--ink);position:relative}
section,header,footer{position:absolute;left:0;width:1200px}

/* Hero */
.hero{top:0;height:740px;overflow:hidden}
.hero-photo{position:absolute;inset:0;background:linear-gradient(180deg,#8fb0c9 0%,#a9bfa4 35%,#6e7f58 60%,#4d5a3a 100%)}
.topbar{position:absolute;top:0;left:0;width:1200px;height:120px;background:rgba(255,255,255,.92)}
.brand{position:absolute;left:100px;top:6px;display:flex;align-items:center;gap:14px}
.brand-circle{width:104px;height:104px;border-radius:50%;border:2px solid #555;display:flex;align-items:center;justify-content:center;text-align:center;font-family:"Cormorant Garamond",Georgia,serif;font-size:18px;line-height:1.05;color:#333;background:#fff}
.call{position:absolute;right:140px;top:18px;font-size:18px;color:var(--call-green);font-weight:700;display:flex;align-items:center;gap:8px}
.social-top{position:absolute;right:40px;top:10px;display:flex;gap:10px}
.social-top span{width:34px;height:34px;border-radius:50%;background:var(--nav-blue);display:block}
.nav{position:absolute;right:40px;top:62px;display:flex;gap:58px;font-family:"Cormorant Garamond",Georgia,serif;font-size:22px;letter-spacing:1px;color:#333}
.nav a{color:inherit;text-decoration:none}
.nav .active{border-bottom:2px solid #333;padding-bottom:4px}
.hero-title{position:absolute;top:308px;width:100%;text-align:center;color:var(--white);font-family:"Cormorant Garamond",Georgia,serif;font-weight:600;font-size:96px;line-height:1;text-shadow:0 2px 8px rgba(0,0,0,.35)}
.hero-sub{position:absolute;top:402px;width:100%;text-align:center;color:var(--white);font-family:"Cormorant Garamond",Georgia,serif;font-size:40px;text-shadow:0 2px 6px rgba(0,0,0,.35)}
.slider{position:absolute;top:632px;left:240px;width:840px;height:3px;background:rgba(255,255,255,.9)}
.slider::after{content:"";position:absolute;left:412px;top:-10px;width:22px;height:22px;border-radius:50%;background:#fff;border:3px solid #333}

/* History */
.history{top:740px;height:820px;background:var(--cream)}
.section-title{font-family:"Cormorant Garamond",Georgia,serif;font-weight:500;font-size:62px;letter-spacing:3px;color:#222;line-height:1}
.history .section-title{position:absolute;left:120px;top:112px}
.body-text{font-size:18px;line-height:1.5;color:var(--ink-soft)}
.history .body-text{position:absolute;left:120px;top:186px;width:600px}
.history-art{position:absolute;left:790px;top:40px;width:380px;height:400px;border-radius:40% 50% 45% 40%;background:radial-gradient(circle,#ece5cf 0%,rgba(239,232,210,0) 70%)}
.nursery-now{position:absolute;left:120px;top:440px;width:960px;height:300px;border-radius:0 90px 0 90px;overflow:hidden;background:linear-gradient(120deg,#6f8a5f 0%,#b4928a 45%,#8aa46f 75%,#5a6c47 100%)}
.nursery-now h2{position:absolute;width:100%;top:112px;text-align:center;color:#fff;font-family:"Cormorant Garamond",Georgia,serif;font-weight:500;font-size:64px;letter-spacing:2px;text-shadow:0 2px 6px rgba(0,0,0,.4)}

/* Native plants */
.native{top:1560px;height:740px;background:var(--white)}
.native-photo{position:absolute;left:0;top:0;width:560px;height:680px;background:linear-gradient(160deg,#3e5a2e 0%,#6c8a45 45%,#2f3a22 100%);clip-path:polygon(0 0,100% 0,82% 100%,0 100%)}
.native .section-title{position:absolute;left:580px;top:160px}
.native .copy{position:absolute;left:580px;top:230px;width:520px}
.native .copy p{margin-bottom:20px}
.lead{font-weight:700;color:var(--ink)}
.btn{display:inline-block;background:var(--teal);color:#fff;font-family:"Cormorant Garamond",Georgia,serif;font-weight:600;font-size:20px;letter-spacing:1px;padding:14px 30px;border-radius:30px;text-decoration:none}
.native .btn{position:absolute;left:580px;top:540px}

/* Flowers */
.flowers{top:2320px;height:560px;background:var(--white)}
.flowers-panel{position:absolute;left:0;top:0;width:660px;height:560px;background:var(--blue-panel);color:#fff}
.flowers-panel .section-title{position:absolute;left:120px;top:70px;color:#fff}
.flowers-panel .body-text{position:absolute;left:120px;top:140px;width:500px;font-size:17px;line-height:1.45;color:#eef3f6}
.flowers-panel .body-text p{margin-bottom:18px}
.flowers-panel .btn{position:absolute;left:120px;top:466px}
.flowers-photo{position:absolute;left:660px;top:0;width:540px;height:560px;background:radial-gradient(circle at 45% 45%,#e58ca6 0%,#c35a7c 35%,#5a7a48 75%,#3c5530 100%)}
.flowers-sprig{position:absolute;left:0;top:500px;width:200px;height:120px;border-radius:50%;background:radial-gradient(ellipse,rgba(255,255,255,.5),rgba(255,255,255,0) 70%)}

/* Giftwear */
.giftwear{top:2880px;height:800px;background:var(--cream)}
.giftwear .section-title{position:absolute;top:80px;width:100%;text-align:center}
.giftwear .intro{position:absolute;left:210px;top:156px;width:780px;text-align:center}
.gift-ring{position:absolute;left:130px;top:250px;width:440px;height:440px;border-radius:50%;border:3px solid var(--teal-dark);padding:14px}
.gift-photo{width:100%;height:100%;border-radius:50%;background:radial-gradient(circle,#e8dcc7 0%,#a9a08c 45%,#4f5c3d 100%)}
.giftwear .copy{position:absolute;left:580px;top:310px;width:520px}
.giftwear .copy p{margin-bottom:20px}
.giftwear .btn{position:absolute;left:580px;top:570px}
.gift-art{position:absolute;right:0;top:460px;width:200px;height:340px;background:radial-gradient(ellipse,#ece5cf 0%,rgba(239,232,210,0) 70%)}

/* Since then */
.since{top:3680px;height:580px;background:var(--green-panel)}
.since-photo{position:absolute;left:600px;top:0;width:600px;height:580px;background:radial-gradient(circle at 50% 50%,#f3efe2 0%,#cfd6b6 40%,#4e7a4a 80%,#2f5436 100%)}
.since-text{position:absolute;left:0;top:0;width:640px;height:580px;background:linear-gradient(90deg,var(--green-panel) 70%,rgba(29,107,85,0) 100%)}
.since h2{position:absolute;left:120px;top:96px;width:480px;color:#fff;font-family:"Cormorant Garamond",Georgia,serif;font-weight:500;font-size:50px;line-height:0.96;letter-spacing:1px}
.since .body-text{position:absolute;left:120px;top:324px;width:440px;font-size:17px;line-height:1.45;color:#eaf3ef}
.since .body-text p{margin-bottom:18px}

/* Footer */
.footer{top:4260px;height:440px;background:var(--footer-bg)}
.footer-logo{position:absolute;left:120px;top:60px;width:210px;height:210px;border-radius:50%;border:2px solid #555;display:flex;align-items:center;justify-content:center;text-align:center;font-family:"Cormorant Garamond",Georgia,serif;font-size:34px;line-height:1.05;color:#333}
.footer h4{font-family:"Cormorant Garamond",Georgia,serif;font-weight:600;font-size:24px;color:#222;margin-bottom:24px}
.f-links{position:absolute;left:396px;top:60px}
.f-links a{display:block;font-size:15px;color:#333;text-decoration:none;margin-bottom:10px}
.f-contact{position:absolute;left:560px;top:60px}
.contact-row{display:flex;align-items:flex-start;gap:14px;font-size:14px;color:#333;margin-bottom:18px;line-height:1.35}
.contact-icon{width:34px;height:34px;border-radius:50%;background:var(--teal);flex:none;display:flex;align-items:center;justify-content:center}
.f-news{position:absolute;left:820px;top:60px;width:280px}
.f-news p{font-size:14px;color:#333;line-height:1.4;margin-bottom:24px}
.email-field{display:flex;align-items:center;justify-content:space-between;border-bottom:1px solid #555;padding-bottom:8px;font-size:14px;color:#333;width:260px}
.send{width:34px;height:34px;border-radius:50%;background:var(--teal);display:flex;align-items:center;justify-content:center}
.f-social{display:flex;gap:10px;margin-top:24px}
.f-social span{width:32px;height:32px;border-radius:50%;border:1.5px solid #444;display:block}
.copyright{position:absolute;left:0;top:376px;width:100%;text-align:center;font-size:13px;color:#555;border-top:1px solid var(--line);padding-top:16px}
</style>
</head>
<body>

<header class="hero">
  <div class="hero-photo" role="img" aria-label="Photograph of the nursery entrance with a timber shed and rows of native plants"></div>
  <div class="topbar">
    <div class="brand"><div class="brand-circle">The<br>Silverbrook<br>Dell</div></div>
    <div class="call">
      <svg width="18" height="18" viewBox="0 0 24 24"><path d="M6.6 10.8a15 15 0 0 0 6.6 6.6l2.2-2.2a1 1 0 0 1 1-.25 11.4 11.4 0 0 0 3.6.57 1 1 0 0 1 1 1V20a1 1 0 0 1-1 1A17 17 0 0 1 3 4a1 1 0 0 1 1-1h3.5a1 1 0 0 1 1 1c0 1.25.2 2.45.57 3.6a1 1 0 0 1-.25 1z" fill="currentColor"/></svg>
      Call Us: 555 010 204
    </div>
    <div class="social-top"><span></span><span></span></div>
    <nav class="nav">
      <a class="active" href="#">HOME</a>
      <a href="#">NURSERY</a>
      <a href="#">NATIVE FLOWERS</a>
      <a href="#">GIFTWEAR</a>
      <a href="#">ABOUT</a>
    </nav>
  </div>
  <h1 class="hero-title">The Silverbrook Dell</h1>
  <p class="hero-sub">Australian Plants * Flowers And Giftware</p>
  <div class="slider"></div>
</header>

<section class="history">
  <div class="history-art" role="img" aria-label="Line drawing of flannel flowers"></div>
  <h2 class="section-title">HISTORY</h2>
  <p class="body-text">The Silverbrook Dell business, that has been providing plants, flowers and native giftware to the Central Coast and surrounding areas since 2001. Over this time, we have established a strong connection with the community and provided expert native advice.</p>
  <div class="nursery-now" role="img" aria-label="Photograph of the nursery today with flowering shrubs along the path">
    <h2>THE NURSERY NOW</h2>
  </div>
</section>

<section class="native">
  <div class="native-photo" role="img" aria-label="Photograph of potted native plants on nursery benches"></div>
  <h2 class="section-title">NATIVE PLANTS</h2>
  <div class="copy body-text">
    <p class="lead">Welcome to our native plant nursery information page!</p>
    <p>At our nursery, we provide native plants that thrive in their local environment. Native plants are essential for preserving biodiversity, and they support pollinators and other wildlife while reducing human impact on the environment.</p>
    <p>At our nursery, we offer a wide selection of native plants that are suitable for a variety of different environments, and we provide planting and care instructions to ensure that your plants thrive once they're in the ground.</p>
  </div>
  <a class="btn" href="#">READ MORE</a>
</section>

<section class="flowers">
  <div class="flowers-panel">
    <h2 class="section-title">FLOWERS</h2>
    <div class="body-text">
      <p>At the nursery, we specialize in creating unique arrangements using locally sourced native Australian flowers. Our team of experienced florists are passionate about showcasing the beauty of our country's flora and fauna through unique and beautiful bespoke floral designs.</p>
      <p>Our native flower arrangements are perfect for any occasion – from weddings and corporate events to simple gifts for loved ones. The vibrant colours and textures of our native flowers can add a touch of the Australian landscape to any space.</p>
    </div>
    <a class="btn" href="#">READ MORE</a>
  </div>
  <div class="flowers-photo" role="img" aria-label="Close-up photograph of a pink grevillea flower"></div>
  <div class="flowers-sprig" role="img" aria-label="Small drawing of white native blossoms"></div>
</section>

<section class="giftwear">
  <h2 class="section-title">GIFTWEAR</h2>
  <p class="intro body-text">We are proud to offer a wide range of unique and high-quality gifts that celebrate the natural beauty of Australia's native flora and fauna. From beautifully scented candles to stunning artworks, our gift selection is sure to please.</p>
  <div class="gift-ring"><div class="gift-photo" role="img" aria-label="Photograph of a native flower arrangement in a ceramic vessel"></div></div>
  <div class="copy body-text">
    <p>Our giftware collection features a range of products that have been designed and crafted by local artisans and small businesses. We believe in supporting our community and showcasing the amazing talent and creativity that can be found here in Australia.</p>
    <p>In addition to our locally made products, we also stock gifts from well-known brands that share our passion for nature and sustainability.</p>
  </div>
  <a class="btn" href="#">READ MORE</a>
  <div class="gift-art" role="img" aria-label="Faint line drawing of native plants"></div>
</section>

<section class="since">
  <div class="since-photo" role="img" aria-label="Photograph of white flannel flower blooms"></div>
  <div class="since-text"></div>
  <h2>SINCE THEN CONCENTRATING STRICTLY ON NATIVE ONLY</h2>
  <div class="body-text">
    <p>The business was originally established by Edda and Maribel, later departed and Tamsin and Corliss</p>
    <p>Edda Lanefield has been in the native plant industry for most of her life. She has been involved in the propagation, wholesale, retail, floral design and promotion of native plants.</p>
  </div>
</section>

<footer class="footer">
  <div class="footer-logo">The<br>Silverbrook<br>Dell</div>
  <div class="f-links">
    <h4>Links</h4>
    <a href="#">Home</a><a href="#">Nursery</a><a href="#">Native flowers</a><a href="#">Giftwear</a><a href="#">About</a>
  </div>
  <div class="f-contact">
    <h4>Contact Us</h4>
    <div class="contact-row"><span class="contact-icon"><svg width="16" height="16" viewBox="0 0 24 24"><path d="M12 2a7 7 0 0 0-7 7c0 5 7 13 7 13s7-8 7-13a7 7 0 0 0-7-7zm0 9.5A2.5 2.5 0 1 1 12 6.5a2.5 2.5 0 0 1 0 5z" fill="#fff"/></svg></span><span>Bushland Road<br>Coastview NSW<br>Australia</span></div>
    <div class="contact-row"><span class="contact-icon"><svg width="16" height="16" viewBox="0 0 24 24"><path d="M6.6 10.8a15 15 0 0 0 6.6 6.6l2.2-2.2a1 1 0 0 1 1-.25 11.4 11.4 0 0 0 3.6.57 1 1 0 0 1 1 1V20a1 1 0 0 1-1 1A17 17 0 0 1 3 4a1 1 0 0 1 1-1h3.5a1 1 0 0 1 1 1c0 1.25.2 2.45.57 3.6a1 1 0 0 1-.25 1z" fill="#fff"/></svg></span><span>Phone 555 013 720</span></div>
    <div class="contact-row"><span class="contact-icon"><svg width="16" height="16" viewBox="0 0 24 24"><path d="M3 5h18v14H3z M3 5l9 7 9-7" fill="none" stroke="#fff" stroke-width="2"/></svg></span><span>hello@silverbrookdell.example</span></div>
  </div>
  <div class="f-news">
    <h4>Newsletter Sign up</h4>
    <p>Join our list for seasonal blooms and nursery news.</p>
    <div class="email-field"><span>Email</span><span class="send"><svg width="16" height="16" viewBox="0 0 24 24"><path d="M4 12h14M13 6l6 6-6 6" fill="none" stroke="#fff" stroke-width="2.4"/></svg></span></div>
    <div class="f-social"><span></span><span></span><span></span><span></span></div>
  </div>
  <div class="copyright">© 2023 All Rights Reserved Terms &amp; Conditions Privacy Policy</div>
</footer>

</body>
</html>
```